Business Card Design

we are a brand new cable TV network devoted to self improvement and leading a better life called FLOURISH TV.I have a logo. We have 3 executives that need cards.I want it to be a heavy stock card: professional but showing our creative nature

Industry/Entity Type

Business

Contact Information for Business Card

CLAUDIA SAENZ AMLIECEO350 San Juan DrPonte Vedra Beach FL 32082904-473-5953

```html
<!DOCTYPE html>
<html lang="en">
<head>
<meta charset="utf-8">
<title>Flourish TV – Business Card</title>
<link rel="stylesheet" href="https://fonts.googleapis.com/css2?family=Poppins:wght@400;600;700&display=swap">
<style>
  :root {
    --page: #e4e4e4;
    --ink: #231f20;
    --black: #0b0b0c;
    --black-soft: #1e1e20;
    --red: #d0151b;
    --red-deep: #a30d12;
    --white: #ffffff;
    --muted: #c9c9c9;
  }
  * { box-sizing: border-box; margin: 0; padding: 0; }
  html, body {
    width: 1200px; height: 1200px; overflow: hidden;
    background: var(--page);
    font-family: "Poppins", sans-serif;
  }
  .sheet {
    position: relative; width: 1200px; height: 1200px;
    display: flex; flex-direction: column; align-items: center; justify-content: center; gap: 70px;
  }
  .card {
    position: relative; width: 760px; height: 434px;
    border-radius: 30px; overflow: hidden;
    box-shadow: 0 14px 30px rgba(0,0,0,0.22);
  }
  /* Front */
  .card--front {
    background: linear-gradient(115deg, var(--black) 0%, var(--black-soft) 48%, var(--black) 100%);
    display: flex; align-items: center; justify-content: center;
  }
  .wordmark { display: flex; align-items: center; gap: 14px; }
  .wordmark__square { width: 48px; height: 48px; background: var(--red); border-radius: 4px; }
  .wordmark__name { font-weight: 600; font-size: 72px; letter-spacing: -1px; line-height: 1; }
  .card--front .wordmark__name { color: var(--white); }

  /* Back */
  .card--back { background: var(--white); }
  .card__waves { position: absolute; inset: 0; width: 100%; height: 100%; }
  .card--back .wordmark { position: absolute; left: 60px; top: 100px; }
  .card--back .wordmark__name { color: var(--ink); font-size: 64px; }
  .card--back .wordmark__square { width: 42px; height: 42px; }
  .contact {
    position: absolute; left: 66px; top: 200px;
    list-style: none; color: var(--ink); font-size: 18px; line-height: 1.35;
  }
  .contact__item { display: flex; gap: 12px; align-items: flex-start; margin-bottom: 4px; }
  .contact__icon { width: 17px; height: 17px; margin-top: 4px; flex: none; }
  .person { position: absolute; right: 40px; top: 262px; text-align: right; }
  .person__name { color: var(--red); font-weight: 700; font-size: 23px; line-height: 1.2; }
  .person__role { color: var(--muted); font-size: 14px; margin-top: 2px; }
</style>
</head>
<body>
<main class="sheet">
  <section class="card card--front" aria-label="Card front">
    <div class="wordmark">
      <span class="wordmark__square"></span>
      <span class="wordmark__name">Flourish TV</span>
    </div>
  </section>

  <section class="card card--back" aria-label="Card back">
    <svg class="card__waves" viewBox="0 0 760 434" preserveAspectRatio="none" aria-hidden="true">
      <path d="M760 60 C620 100 540 230 430 300 C340 360 230 410 140 434 L760 434 Z" fill="var(--black)"/>
      <path d="M760 40 C610 84 522 214 412 284 C310 348 180 400 0 414" fill="none" stroke="var(--red)" stroke-width="11"/>
      <path d="M760 24 C600 70 506 200 396 270 C292 336 160 388 0 400" fill="none" stroke="var(--red-deep)" stroke-width="3"/>
      <path d="M0 427 C170 421 300 392 432 300" fill="none" stroke="var(--black)" stroke-width="10"/>
    </svg>

    <div class="wordmark">
      <span class="wordmark__square"></span>
      <span class="wordmark__name">Flourish TV</span>
    </div>

    <ul class="contact">
      <li class="contact__item">
        <svg class="contact__icon" viewBox="0 0 24 24" aria-hidden="true"><path fill="var(--red)" d="M6.6 10.8a15.1 15.1 0 0 0 6.6 6.6l2.2-2.2a1 1 0 0 1 1-.25 11.4 11.4 0 0 0 3.6.57 1 1 0 0 1 1 1V20a1 1 0 0 1-1 1A17 17 0 0 1 3 4a1 1 0 0 1 1-1h3.5a1 1 0 0 1 1 1c0 1.25.2 2.45.57 3.57a1 1 0 0 1-.25 1z"/></svg>
        <span>555-218-0476</span>
      </li>
      <li class="contact__item">
        <svg class="contact__icon" viewBox="0 0 24 24" aria-hidden="true"><path fill="var(--red)" d="M12 2a7 7 0 0 0-7 7c0 5.2 7 13 7 13s7-7.8 7-13a7 7 0 0 0-7-7zm0 9.5A2.5 2.5 0 1 1 12 6.5a2.5 2.5 0 0 1 0 5z"/></svg>
        <span>718 Copper Hollow Ln<br>Marlow Cove Beach FL 30915</span>
      </li>
    </ul>

    <div class="person">
      <p class="person__name">Marisol Duval Kerno</p>
      <p class="person__role">CEO</p>
    </div>
  </section>
</main>
</body>
</html>
```